Business Card Design Project

I require a business card for a new coaching business based in Melbourne with global clients. Both companies and individuals will retain our coaching services.

Target Market(s)

Both small business and large corporate in western speaking countries. Individuals requiring support and direction on issues such as fears, phobias, career, relationships, confidence, self esteem etc.

Industry/Entity Type

Business

Font styles to use
Sans Serif

Colors

Designer to choose colors to be used in the design.

Requirements
Must have
• White background to enhance the colours in the logo. Logo on the left.
Should not have
• The black and white version of the logo. Keep the colours.

```html
<!DOCTYPE html>
<html lang="en">
<head>
<meta charset="utf-8">
<title>Clear Summit Coaching – Business Card</title>
<link rel="stylesheet" href="https://fonts.googleapis.com/css2?family=Baloo+2:wght@400;500;600;700&display=swap">
<style>
  :root {
    --pink: #ea0a72;
    --orange: #f58b1f;
    --green: #92c83e;
    --blue: #1a85c8;
    --grey-text: #6d6e71;
    --card-white: #ffffff;
    --stage: #5e5e5e;
  }
  * { box-sizing: border-box; margin: 0; padding: 0; }
  html, body {
    width: 1200px;
    height: 960px;
    overflow: hidden;
    background: var(--stage);
    font-family: "Baloo 2", sans-serif;
  }
  .canvas { position: relative; width: 1200px; height: 960px; }

  .card {
    position: absolute;
    width: 640px;
    height: 394px;
  }
  .card--front { left: 62px; top: 56px; }
  .card--back  { left: 487px; top: 509px; height: 396px; }

  .card__border {
    position: absolute;
    inset: 0;
    background: linear-gradient(135deg, var(--pink) 0%, var(--orange) 35%, var(--green) 65%, var(--blue) 100%);
  }
  .card__panel {
    position: absolute;
    background: var(--card-white);
  }
  .card--front .card__panel { left: 34px; right: 35px; top: 0; bottom: 33px; }
  .card--back .card__panel  { left: 34px; right: 35px; top: 35px; bottom: 33px; }

  .brand-mark {
    position: absolute;
    left: 55px; top: 40px;
    width: 100px; height: 100px;
    border-radius: 50%;
    background: var(--orange);
  }
  .brand-name {
    position: absolute;
    left: 199px; top: 38px;
    font-weight: 600;
    font-size: 36px;
    line-height: 34px;
    color: var(--grey-text);
    text-transform: uppercase;
    letter-spacing: -0.5px;
  }

  .person-name {
    position: absolute;
    left: 196px; top: 160px;
    font-weight: 400;
    font-size: 33px;
    line-height: 1;
    color: var(--pink);
  }
  .person-title {
    position: absolute;
    left: 197px; top: 199px;
    font-size: 16px;
    line-height: 1;
    color: var(--pink);
  }

  .contact-rule {
    position: absolute;
    left: 15px; top: 287px;
    width: 531px; height: 3px;
    background: var(--pink);
  }
  .contact {
    position: absolute;
    font-size: 17px;
    font-weight: 600;
    line-height: 1;
    color: var(--orange);
    white-space: nowrap;
  }
  .contact__label { color: var(--blue); }
  .contact__sep { color: var(--blue); font-weight: 400; margin: 0 3px; }
  .contact--phone { left: 15px; top: 302px; }
  .contact--abn   { right: 25px; top: 302px; }
  .contact--email { left: 22px; top: 331px; }

  .tagline {
    position: absolute;
    left: 0; right: 0;
    top: 143px;
    text-align: center;
    font-weight: 700;
    font-size: 29px;
    line-height: 1.2;
    color: var(--pink);
  }
</style>
</head>
<body>
<main class="canvas">

  <section class="card card--front" aria-label="Business card front">
    <div class="card__border" role="img" aria-label="Multicoloured border band in pink, orange, green and blue"></div>
    <div class="card__panel">
      <div class="brand-mark" aria-hidden="true"></div>
      <p class="brand-name">Clear<br>Summit<br>Coaching</p>

      <h1 class="person-name">Lena Marlowe-Hart</h1>
      <p class="person-title">Performance Consultant and Coach</p>

      <div class="contact-rule"></div>
      <p class="contact contact--phone"><span class="contact__label">PHONE</span><span class="contact__sep">|</span> +61 (0) 400 555 182</p>
      <p class="contact contact--abn"><span class="contact__label">ABN</span><span class="contact__sep">|</span> 51824753901</p>
      <p class="contact contact--email"><span class="contact__label">EMAIL</span><span class="contact__sep">|</span> lena.hart@example.com</p>
    </div>
  </section>

  <section class="card card--back" aria-label="Business card back">
    <div class="card__border" role="img" aria-label="Multicoloured border band in pink, orange, green and blue"></div>
    <div class="card__panel">
      <p class="tagline">The mind is more powerful than the body.</p>
    </div>
  </section>

</main>
</body>
</html>
```